Briarwick Dale Half Marathon 2015

I am in need of a 2 sided promotional print postcard for our half marathon held in March. The print is distributed in October.

Must include running stick figure, Corlandt Vee Bridge and lighthouse in design. These elements can be seen in the uploaded design from last year. Also, the Stonemill Striders Logo and Ashgrove logo must be on it.

Saturday, March 21st at 9:30am
Register on RACELY.example
Register before end of 2014 and recieve $5 off registration - Use coupon code BK7948

Back of the post card to include details:

Registration fee $60 until 3/13/14, race day $70
Race start/finish is walking distance from the train -Valeway Coastal Line to Millbrook Station
Finisher Goodie bag
LS technical shirt
Electronic timing
NRFB Certified course
Water and Quenchix fluid stations
CASH awards to top 3 overall male and female finishers
Awards and prizes to top category finishers
Each finisher will receive a 2014 Briarwick Dale Half Marathon medal, sponsored by Ashgrove Memorial Hospital Center

Target Market(s)

These are males and females ages 21-55

Industry/Entity Type

Electronic

Colors
33a6d7
34b8a4
faee3f
add136
3176b5
f04a50

Requirements
Must have
• 2 logos
name - Briarwick Dale Half Marathon
date
www.stonemillstriders.example
2 sided with detailed info on back and general info on front

```html
<!DOCTYPE html>
<html lang="en">
<head>
<meta charset="utf-8">
<title>Briarwick Dale Half Marathon 2015 – Postcard</title>
<link href="https://fonts.googleapis.com/css2?family=Marcellus&display=swap" rel="stylesheet">
<style>
  :root {
    --page: #ffffff;
    --sky-top: #b9c3cf;
    --sky-mid: #d6dce3;
    --water: #8e9aa6;
    --shore: #5b5550;
    --headline: #c3262c;
    --headline-shadow: rgba(40, 10, 10, 0.55);
    --back-border: #7a1a22;
    --front-border: #9aa3ad;
    --panel: #dbeef6;
    --logo-bg: #ffffff;
    --logo-ink: #1f4f9c;
    --logo-accent: #33a6d7;
  }
  * { box-sizing: border-box; margin: 0; padding: 0; }
  html, body { width: 1200px; height: 1150px; overflow: hidden; background: var(--page); }
  body { position: relative; font-family: "Marcellus", serif; }

  .postcard {
    position: absolute;
    left: 15px;
    width: 1170px;
    overflow: hidden;
  }
  .postcard--front { top: 5px; height: 570px; border: 2px solid var(--front-border); }
  .postcard--back { top: 590px; height: 552px; border: 4px solid var(--back-border); border-radius: 14px; }

  .scene {
    position: absolute; inset: 0;
    background:
      linear-gradient(180deg, var(--sky-top) 0%, var(--sky-mid) 45%, var(--water) 70%, var(--shore) 100%);
  }

  .logo {
    position: absolute; top: 12px;
    height: 130px;
    background: var(--logo-bg);
    display: flex; align-items: center; justify-content: center; gap: 10px;
    color: var(--logo-ink);
    font-size: 28px;
    text-align: center;
    line-height: 1.05;
  }
  .logo--sponsor { left: 840px; width: 170px; }
  .logo--club { left: 1020px; width: 140px; font-size: 24px; }
  .logo__mark { width: 22px; height: 22px; border-radius: 50%; background: var(--logo-accent); flex: none; }

  .runner-panel {
    position: absolute; left: 950px; width: 210px; height: 230px;
    background: var(--panel);
  }
  .postcard--front .runner-panel { top: 170px; }
  .postcard--back .runner-panel { top: 190px; }

  .headline {
    position: absolute;
    color: var(--headline);
    text-shadow: 1px 1px 2px var(--headline-shadow);
  }
  .headline span { display: block; }
  .race-title { left: 10px; top: 300px; font-size: 44px; line-height: 48px; }
  .front-info { left: 10px; top: 365px; font-size: 31px; line-height: 32px; }
  .back-details { left: 10px; top: 40px; font-size: 27px; line-height: 32.5px; }
</style>
</head>
<body>

<section class="postcard postcard--front">
  <div class="scene" role="img" aria-label="Photo of the Corlandt Vee Bridge over the river with a lighthouse in the foreground"></div>
  <div class="logo logo--sponsor"><span class="logo__mark"></span>Ashgrove</div>
  <div class="logo logo--club">Stonemill<br>Striders</div>
  <div class="runner-panel" role="img" aria-label="Running stick figure illustration"></div>
  <h1 class="headline race-title">Briarwick Dale Half Marathon 2015</h1>
  <p class="headline front-info">
    <span>Saturday, March 21st at 9:30am</span>
    <span>Register on RACELY.example</span>
    <span>Register before end of 2014 and recieve $5 off registration</span>
    <span>- Use coupon code BK7948</span>
    <span>www.stonemillstriders.example</span>
  </p>
</section>

<section class="postcard postcard--back">
  <div class="scene" role="img" aria-label="Photo of the lighthouse on the river beside the Corlandt Vee Bridge"></div>
  <div class="logo logo--sponsor"><span class="logo__mark"></span>Ashgrove</div>
  <div class="logo logo--club">Stonemill<br>Striders</div>
  <div class="runner-panel" role="img" aria-label="Running stick figure illustration"></div>
  <p class="headline back-details">
    <span>Registration fee $60 until 3/13/14, race day $70</span>
    <span>Race start/finish is walking distance from the train -</span>
    <span>Valeway Coastal Line to Millbrook Station</span>
    <span>Finisher Goodie bag</span>
    <span>LS technical shirt</span>
    <span>Electronic timing</span>
    <span>NRFB Certified course</span>
    <span>Water and Quenchix fluid stations</span>
    <span>CASH awards to top 3 overall male and female</span>
    <span>finishers</span>
    <span>Awards and prizes to top category finishers</span>
    <span>Each finisher will receive a 2014 Briarwick Dale Half</span>
    <span>Marathon medal, sponsored by Ashgrove Memorial Hospital</span>
    <span>Center</span>
  </p>
</section>

</body>
</html>
```